Harbor Outreach company is looking for a web page design

Your projects should contain:

1. Header: Logo provided by us.
2. Top nav bar: offer, about us, experience, contact.
3. “Choose language” button.
4. Main section: panoramic picture (static, professional, modern).
5. Below section: 3 blocks (image+title+description), which represent our 3 main activities (titles):
• Market Research,
• Marketing Plans,
• Marketing Project.
6. ‘Contact us’ form – Message (text: “Write your message and give us details about your company and activities”), Email, SEND).
7. Page footer: (4 section: Contact, Social Media, Blog, Partners).

Hello!

I uploaded new file 'general_look', which is our idea how the page should generally look like.

BUT! it doesn't mean that your projects should look exactly like this project e.g.:
* titles Market Research, Marketing Plans, Marketing Project can be above these: Image 1,2,3.
* everything doesn't have to be in square and rectangle shape. You can try to manipulate with blocks and can add elipse elemnts or something similar.

We will appreciate your innovative ideas. Just wanted to give you general plan of the site and ilustrate all elements that we require.

Best Regards,
Tomas

IMPORTENT

Please remember that the main picture should be panoramic. Please do not close it in frame.

Small and middle sized companies, which would like to export their goods and services abroad and are interested in raising funds from European Union to expand their activities. These are rather industrial companies with low level of innovativeness. Our mission is to build image of the client’s company and increase awareness of their products to improve their competitiveness and innovativeness.

It Company

• 1. Create designs of main page and subpage.
2. Subpage: Logo, Header, language button, place for article, navigation menu on the right side - below it “contact us” button , footer on the bottom. (In this section we are looking mainly for the design of the header and navigation menu).
3. The whole design should be a series of horizontal blocks.
4. Your projects should be associated with features such as: Reliability, Security, Professionalism, Openness, Uniqueness.
5. The design should be simple, fresh, readable, easy to use and should create a feeling of high quality services.
6. Possibility to change the panoramic picture (separate layer in a graphic file).
7. All pictures and blocks should be static, no movements.
8. Style of the page should be compliant with the logo design, font: Swiss.
9. Designs that we like: http://www.quillbrand-studio.pl/, http://www.zephyrlane-example.com/.
• There shouldn’t be any distractions and not matching parts (whole design should be compact and easy to interpret and remember).

```html
<!DOCTYPE html>
<html lang="en">
<head>
<meta charset="utf-8">
<title>Harbor Outreach</title>
<link href="https://fonts.googleapis.com/css2?family=PT+Sans:wght@400;700&display=swap" rel="stylesheet">
<style>
:root{
  --ink:#222;
  --text:#333;
  --muted:#666;
  --accent:#e0500e;
  --brand:#1a5a8a;
  --sky-top:#5fb0ef;
  --sky-mid:#a9d4f6;
  --band-dark:#333333;
  --band-mid:#4a4a4a;
  --footer:#f2f2f2;
  --bullet:#f2a37a;
  --white:#fff;
}
*{box-sizing:border-box;margin:0;padding:0}
html,body{width:1200px;height:966px;overflow:hidden;background:var(--white);font-family:"PT Sans",sans-serif;color:var(--text)}
.page{position:relative;width:1200px;height:966px}
.site-header{position:absolute;left:0;top:0;width:1200px;height:47px;background:var(--white);z-index:3}
.brand{position:absolute;left:4px;top:9px;display:flex;align-items:center;gap:7px;font-size:21px;color:var(--brand);letter-spacing:-.3px}
.brand-dot{width:26px;height:26px;border-radius:50%;background:var(--brand)}
.main-nav{position:absolute;left:560px;top:13px;display:flex}
.main-nav a{display:block;padding:2px 23px;font-size:13px;font-weight:700;color:var(--ink);text-decoration:none;border-left:1px solid #ddd;letter-spacing:.3px}
.main-nav a:first-child{border-left:none}
.hero{position:absolute;left:0;top:47px;width:1200px;height:290px;background:linear-gradient(180deg,var(--sky-top) 0%,var(--sky-mid) 55%,var(--white) 100%)}
.hero-map{position:absolute;left:0;top:0;width:700px;height:338px;background:radial-gradient(ellipse at 45% 45%,#1f6fa3 0%,#2c7fb4 45%,rgba(60,140,195,0) 75%);opacity:.85}
.hero-people{position:absolute;left:625px;top:8px;width:340px;height:267px;background:linear-gradient(180deg,#c8d9e8 0%,#4a4f58 55%,#2c2f36 100%);border-radius:120px 120px 0 0}
.hero-title{position:absolute;left:227px;top:189px;font-size:17px;font-weight:700;color:#111;letter-spacing:.3px}
.container{position:absolute;left:222px;top:322px;width:757px;height:631px;background:var(--white);box-shadow:0 0 2px rgba(0,0,0,.25)}
.services{display:flex;height:129px}
.service{position:relative;color:var(--white);background:var(--band-dark)}
.service:nth-child(1){width:249px}
.service:nth-child(2){width:258px;background:var(--band-mid)}
.service:nth-child(3){width:250px}
.service-icon{position:absolute;left:14px;top:17px;width:44px;height:46px}
.service h2{position:absolute;left:63px;top:19px;font-size:17px;font-weight:700;letter-spacing:.2px}
.service p{position:absolute;left:63px;top:52px;font-size:10px;font-weight:700;line-height:14px}
.service:nth-child(1) p{width:150px}
.service:nth-child(2) p{width:165px}
.service:nth-child(3) p{width:180px}
.more{position:absolute;top:89px;width:53px;height:23px;border-radius:12px;background:linear-gradient(#fff,#d9d9d9);color:#333;font-size:10px;text-align:center;line-height:23px}
.service:nth-child(1) .more{left:98px}
.service:nth-child(2) .more{left:103px}
.service:nth-child(3) .more{left:98px}
.content{position:relative;height:355px}
.col-title{font-size:20px;font-weight:400;color:var(--muted);line-height:26px}
.news{position:absolute;left:15px;top:18px;width:165px}
.news .col-title{margin-bottom:6px}
.news-item{border-bottom:1px solid #ddd;padding-bottom:9px;margin-bottom:13px}
.news-item:last-child{border:none}
.news-date{font-size:13px;color:var(--accent);line-height:17px;margin-bottom:8px}
.news-item p{font-size:10px;line-height:14.5px}
.contact{position:absolute;left:204px;top:18px;width:345px;height:330px;font-size:10px}
.contact > *{position:absolute;left:0}
.contact .col-title{top:0}
.contact .intro{top:36px}
.label-name{top:59px}
.field-name{top:81px}
.label-email{top:113px}
.field-email{top:125px}
.label-comments{top:157px}
.area{top:169px}
.submit{top:299px}
.field{width:111px;height:16px;border:1px solid #ccc}
.area{width:342px;height:115px;border:1px solid #ccc}
.submit{width:62px;height:23px;border-radius:12px;border:1px solid #bbb;background:linear-gradient(#fff,#ddd);font:10px "PT Sans",sans-serif;color:#333}
.highlights{position:absolute;left:583px;top:18px;width:165px}
.highlights ul{list-style:none;margin-top:6px}
.highlights li{position:relative;padding-left:19px;font-size:10px;line-height:18.2px}
.highlights li::before{content:"";position:absolute;left:2px;top:6px;width:7px;height:7px;border:1.5px solid var(--bullet);border-radius:50%}
.site-footer{position:absolute;left:0;top:484px;width:757px;height:147px;background:var(--footer)}
.foot-col{position:absolute;top:15px}
.foot-col h3{font-size:13px;font-weight:400;color:var(--muted);margin-bottom:8px}
.foot-col a{display:block;font-size:9px;color:var(--accent);text-decoration:none;line-height:12.3px}
.social{display:flex;gap:8px;margin-top:2px}
.social span{width:24px;height:24px;border-radius:5px}
.flags{position:absolute;left:15px;top:99px;display:flex;gap:2px}
.flags span{display:block;width:20px;height:12px;border:1px solid #999}
.copyright{position:absolute;left:570px;top:110px;font-size:9px;color:var(--muted)}
</style>
</head>
<body>
<div class="page">
  <header class="site-header">
    <div class="brand"><span class="brand-dot"></span>Harbor Outreach</div>
    <nav class="main-nav">
      <a href="#">OFFER</a><a href="#">ABOUT US</a><a href="#">EXPERIENCE</a><a href="#">CONTACT US</a>
    </nav>
  </header>

  <section class="hero">
    <div class="hero-map" role="img" aria-label="World map in deep blue across the sky"></div>
    <div class="hero-people" role="img" aria-label="Two business people in suits looking ahead with documents"></div>
    <h1 class="hero-title">YOUR PASSPORT TO FOREIGN MARKETS</h1>
  </section>

  <main class="container">
    <section class="services">
      <article class="service">
        <div class="service-icon" role="img" aria-label="Green book icon" style="background:linear-gradient(#7ec04a,#3d7a22);border-radius:4px"></div>
        <h2>MARKET RESEARCH</h2>
        <p>Lorem ipsum dolor sit amet, consectetur .</p>
        <span class="more">More</span>
      </article>
      <article class="service">
        <div class="service-icon" role="img" aria-label="Brown briefcase icon" style="background:linear-gradient(#c8743a,#8a4418);border-radius:5px;top:22px;height:40px"></div>
        <h2>MARKETING PLANS</h2>
        <p>Cras elit nisl, rhoncus nec iaculis rhoncus.</p>
        <span class="more">More</span>
      </article>
      <article class="service">
        <svg class="service-icon" viewBox="0 0 46 46" role="img" aria-label="Pie chart icon">
          <circle cx="23" cy="23" r="21" fill="#e8632e"/>
          <path d="M23 23 L23 2 A21 21 0 0 1 44 23 Z" fill="#f2c230"/>
          <path d="M23 23 L44 23 A21 21 0 0 1 28 43 Z" fill="#3a8fd8"/>
          <path d="M23 23 L2 23 A21 21 0 0 1 23 2 Z" fill="#8cc63f"/>
        </svg>
        <h2>MARKETING PROJECT</h2>
        <p>Aenean sollicitudin arcu&nbsp; pellentesque ac iaculis.</p>
        <span class="more">More</span>
      </article>
    </section>

    <div class="content">
      <section class="news">
        <h2 class="col-title">Latest News</h2>
        <div class="news-item"><div class="news-date">04/01/2011</div><p>Lorem ipsum dolor sit amet,<br>consectetur adipiscing<br>elit. Pellentesque ac felis<br>tellus. Donec ut hendrerit enim.</p></div>
        <div class="news-item"><div class="news-date">03/17/2011</div><p>Etiam pharetra, tellus sit amet<br>congue vulputate, nisi erat iaculis<br>nibh, vitae feugiat sapien ante<br>eget mauris.</p></div>
        <div class="news-item"><div class="news-date">02/21/2011</div><p>Cras elit nisl, rhoncus nec iaculis<br>ultricies, feugiat eget sapien.<br>Pellentesque ac felis tellus.</p></div>
      </section>

      <section class="contact">
        <h2 class="col-title">Contact US</h2>
        <p class="intro">Write your message and give details about your company and activities.</p>
        <label class="label-name">Your name:</label><div class="field field-name"></div>
        <label class="label-email">Your email:</label><div class="field field-email"></div>
        <label class="label-comments">Your comments:</label><div class="area"></div>
        <button class="submit">Submit</button>
      </section>

      <section class="highlights">
        <h2 class="col-title">Highlights</h2>
        <ul>
          <li>Lorem ipsum dolor sit amet</li><li>Consectetur adipiscing elit</li><li>Etiam pharetra tellus sit</li>
          <li>Amet congue vulputate</li><li>Nisi erat iaculis cras elit nisl</li><li>Rhoncus nec iaculis ultricies</li>
          <li>Pellentesque ac felis tellus</li><li>Aenean sollicitudin</li><li>Arcu duis placerat justo</li>
          <li>Interdum ultrices phasellus</li><li>Elit dolor consectetur</li><li>Sit amet, posuere id magna</li>
          <li>Duis placerat justo eu nunc</li><li>Interdum ultrices phasellus</li>
        </ul>
      </section>
    </div>

    <footer class="site-footer">
      <div class="foot-col" style="left:15px"><h3>Contact</h3><a href="#">Contact Us</a><a href="#">About Us</a><a href="#">Management</a></div>
      <div class="foot-col" style="left:148px"><h3>Partners</h3><a href="#">Partner 1</a><a href="#">Partner 2</a><a href="#">Partner 3</a></div>
      <div class="foot-col" style="left:281px"><h3>Location</h3><a href="#">Area Map</a><a href="#">Address</a></div>
      <div class="foot-col" style="left:414px"><h3>Blog</h3><a href="#">Current Events</a><a href="#">Terms</a></div>
      <div class="foot-col" style="left:570px"><h3>Social Media</h3><a href="#" style="line-height:9px">Terms</a>
        <div class="social"><span style="background:#f07a1e"></span><span style="background:#3fb3e0"></span><span style="background:#3b5998"></span></div>
      </div>
      <div class="flags">
        <span style="background:linear-gradient(90deg,#0a3a9a 33%,#fff 33% 66%,#e01e2e 66%)"></span>
        <span style="background:linear-gradient(#000 33%,#d00 33% 66%,#fc0 66%)"></span>
        <span style="background:linear-gradient(90deg,#1a9a3a 33%,#fff 33% 66%,#d01e2e 66%)"></span>
        <span style="background:#2a9a3a"></span>
        <span style="background:linear-gradient(#c8102e 25%,#fc0 25% 75%,#c8102e 75%)"></span>
        <span style="background:#fff"></span>
        <span style="background:#fff"></span>
        <span style="background:#de2910"></span>
        <span style="background:#1a7a3a"></span>
      </div>
      <div class="copyright">Copyright © 2011 All Rights Reserved.</div>
    </footer>
  </main>
</div>
</body>
</html>
```